CASH PAYMENT DISCOUNT NOTICE POSTED IN CASH REGISTER AREA

LOOKING TO MAKE A FLYER OR A POSTED NOTICE FOR CUSTOMERS PAYING FOR OVER-THE-COUNTER MERCHANDISE AND WHO PAY BY CASH METHOD TO GET A 4% CASH DISCOUNT.
PRESCRIPTIONS ARE EXCLUDED FROM THIS CASH DISCOUNT.

Target Market(s)

RETAIL CUSTOMERS

Industry/Entity Type

RETAIL PHARMACY

Colors
0054AA
0677BA
7BADD7
CADEEF
E8F1F8
EB3D1F
EC4F4E
F09395
F8D3D4
FCEDEE

Requirements
Must have
• LOGO COLORS
Nice to have
• EYE CATCHING

```html
<!DOCTYPE html>
<html lang="en">
<head>
<meta charset="utf-8">
<title>Cash Payment Discount – Kestrel Pharmacy</title>
<link rel="stylesheet" href="https://fonts.googleapis.com/css2?family=Montserrat:wght@400;600;700;800;900&display=swap">
<style>
  :root {
    --stage: #d9d9d9;
    --white: #ffffff;
    --red: #b3202a;
    --red-dark: #8a171d;
    --blue: #1d3f95;
    --blue-dark: #0e2463;
    --brand-blue: #2a4fa8;
    --photo-light: #e8f1f8;
    --photo-mid: #cadeef;
    --photo-deep: #7badd7;
  }
  * { box-sizing: border-box; margin: 0; padding: 0; }
  html, body { width: 1200px; height: 2249px; overflow: hidden; background: var(--stage); }
  body { position: relative; font-family: "Montserrat", sans-serif; }

  .flyer {
    position: absolute; left: 60px; top: 425px; width: 1080px; height: 1398px;
    background: linear-gradient(180deg, var(--blue) 0%, var(--blue-dark) 100%);
    box-shadow: 0 20px 40px rgba(0,0,0,.3);
    overflow: hidden;
  }
  .brand-header {
    position: absolute; left: 0; top: 0; width: 100%; height: 217px;
    background: var(--white);
    display: flex; align-items: center; justify-content: center; gap: 22px;
  }
  .brand-mark { width: 46px; height: 46px; border-radius: 50%; background: var(--brand-blue); }
  .brand-name { font-size: 58px; font-weight: 700; color: var(--brand-blue); letter-spacing: 1px; }

  .title-band {
    position: absolute; left: 0; top: 217px; width: 100%; height: 280px;
    background: linear-gradient(180deg, var(--red) 0%, var(--red-dark) 100%);
  }
  .title {
    position: absolute; left: 0; width: 100%; text-align: center; color: var(--white);
    font-weight: 800; line-height: 1;
  }
  .title-top { top: 250px; font-size: 76px; letter-spacing: 1px; }
  .title-main { top: 318px; font-size: 132px; font-weight: 900; letter-spacing: 1px; }

  .photo-frame {
    position: absolute; left: 69px; top: 445px; width: 945px; height: 405px;
    border: 9px solid var(--white); border-radius: 22px;
    background: linear-gradient(90deg, var(--photo-light) 0%, var(--white) 35%, var(--photo-mid) 70%, var(--photo-deep) 100%);
    box-shadow: 0 6px 18px rgba(0,0,0,.35);
  }

  .offer-text {
    position: absolute; left: 82px; top: 876px; width: 480px;
    color: var(--white); font-size: 41px; line-height 1.18; line-height: 48px; font-weight: 400;
  }
  .offer-text strong { font-weight: 800; }

  .discount-badge {
    position: absolute; left: 348px; top: 1019px; width: 178px; height: 178px;
    border-radius: 50%; border: 4px solid var(--white); overflow: hidden;
    background: linear-gradient(180deg, var(--red) 0%, var(--red) 55%, var(--blue) 55%, var(--blue) 100%);
    color: var(--white); text-align: center;
    box-shadow: 0 6px 12px rgba(0,0,0,.35);
  }
  .badge-kicker { margin-top: 22px; font-size: 20px; font-weight: 600; }
  .badge-value { font-size: 62px; font-weight: 900; line-height: 1; }
  .badge-label { margin-top: 6px; font-size: 20px; font-weight: 800; line-height: 1.05; }

  .divider {
    position: absolute; left: 563px; top: 890px; width: 2px; height: 300px;
    background: rgba(255,255,255,.35);
  }

  .services-heading {
    position: absolute; left: 600px; top: 888px; width: 376px; height: 48px;
    background: var(--red); border-left: 6px solid var(--red-dark); border-radius: 0 14px 14px 0;
    color: var(--white); font-size: 31px; font-weight: 800; line-height: 48px; padding-left: 20px;
  }
  .services-list {
    position: absolute; left: 604px; top: 950px; list-style: none;
    color: var(--white); font-size: 23px; font-weight: 600;
  }
  .services-list li { display: flex; align-items: center; gap: 11px; height: 36px; }
  .services-list svg { width: 16px; height: 16px; flex: none; }

  .exclusion-note {
    position: absolute; left: 78px; top: 1223px; width: 921px; height: 104px;
    background: linear-gradient(180deg, var(--red) 0%, var(--red-dark) 100%);
    border: 2px solid var(--white); border-radius: 16px;
    color: var(--white); text-align: center; font-size: 38px; font-weight: 800; line-height: 44px;
    padding-top: 8px;
    box-shadow: 0 6px 14px rgba(0,0,0,.35);
  }
</style>
</head>
<body>
  <main class="flyer">
    <header class="brand-header">
      <span class="brand-mark"></span>
      <span class="brand-name">Kestrel Pharmacy</span>
    </header>

    <section class="title-band"></section>
    <h1 class="title title-top">CASH PAYMENT</h1>
    <h2 class="title title-main">DISCOUNT</h2>

    <div class="photo-frame" role="img" aria-label="Photo of a pharmacist in a white coat standing by bright shelves of over-the-counter products"></div>

    <p class="offer-text">For customers paying for <strong>over-the-counter merchandise</strong><br>and who pay<br>by cash<br>method to</p>

    <div class="discount-badge">
      <div class="badge-kicker">GET A</div>
      <div class="badge-value">4%</div>
      <div class="badge-label">CASH<br>DISCOUNT</div>
    </div>

    <div class="divider"></div>

    <div class="services-heading">SPECIALTY SERVICES</div>
    <ul class="services-list">
      <li><svg viewBox="0 0 16 16"><circle cx="8" cy="8" r="8" fill="#fff"/><path d="M4.5 8.3l2.3 2.2 4.7-4.8" fill="none" stroke="#1d3f95" stroke-width="2"/></svg>Well-Being Program</li>
      <li><svg viewBox="0 0 16 16"><circle cx="8" cy="8" r="8" fill="#fff"/><path d="M4.5 8.3l2.3 2.2 4.7-4.8" fill="none" stroke="#1d3f95" stroke-width="2"/></svg>Medication Flavoring</li>
      <li><svg viewBox="0 0 16 16"><circle cx="8" cy="8" r="8" fill="#fff"/><path d="M4.5 8.3l2.3 2.2 4.7-4.8" fill="none" stroke="#1d3f95" stroke-width="2"/></svg>Multi-dose Packaging</li>
      <li><svg viewBox="0 0 16 16"><circle cx="8" cy="8" r="8" fill="#fff"/><path d="M4.5 8.3l2.3 2.2 4.7-4.8" fill="none" stroke="#1d3f95" stroke-width="2"/></svg>Monthly Refill Synchronized Program</li>
      <li><svg viewBox="0 0 16 16"><circle cx="8" cy="8" r="8" fill="#fff"/><path d="M4.5 8.3l2.3 2.2 4.7-4.8" fill="none" stroke="#1d3f95" stroke-width="2"/></svg>Diabetes Screening</li>
      <li><svg viewBox="0 0 16 16"><circle cx="8" cy="8" r="8" fill="#fff"/><path d="M4.5 8.3l2.3 2.2 4.7-4.8" fill="none" stroke="#1d3f95" stroke-width="2"/></svg>Blood Sugar Screening</li>
      <li><svg viewBox="0 0 16 16"><circle cx="8" cy="8" r="8" fill="#fff"/><path d="M4.5 8.3l2.3 2.2 4.7-4.8" fill="none" stroke="#1d3f95" stroke-width="2"/></svg>Diagnostic Training</li>
    </ul>

    <div class="exclusion-note">PRESCRIPTIONS ARE EXCLUDED FROM THIS<br>CASH DISCOUNT</div>
  </main>
</body>
</html>
```